Would like a design for lawn signs I will be using to advertise with. Attached are three images. One is the jpeg version of our logo to use in creating and editing the design. The other two are mock ups of our current style of tshirt and business card design. I would like the finished product to look similar in style to the mock ups. The actual color of our logo in the jpeg picture is outdated coloring. I would like the logo to be the color of the logo in the mock up tshirt version and the business card design.
The signs I will be using are white in color and 18"x24" white lawn signs, so I would like the logo to appear like the logo in the grey tshirt design, where it is black and orange. As for the text coloring I would like it to be black as well.
The only things I want included on the text of the sign design is:
Phone: 816-402-7761
Email: tidyturfco@fernmail.com
Mowing
Fertilization
Aeration
Bed & tree maintenance
and more.

```html
<!DOCTYPE html>
<html lang="en">
<head>
<meta charset="utf-8">
<title>Tidy Turf Co — Lawn Sign</title>
<link rel="stylesheet" href="https://fonts.googleapis.com/css2?family=Graduate&family=Oswald:wght@400;500&display=swap">
<style>
  :root {
    --ink: #121212;
    --accent: #ee4b43;
    --paper: #ffffff;
  }
  * { margin: 0; padding: 0; box-sizing: border-box; }
  html, body { width: 1200px; height: 900px; overflow: hidden; background: var(--paper); }
  .sign {
    position: relative;
    width: 1200px;
    height: 900px;
    background: var(--paper);
    color: var(--ink);
    font-family: "Graduate", serif;
  }
  .brand {
    position: absolute;
    left: 0; right: 0;
    top: 160px;
    display: flex;
    justify-content: center;
    align-items: center;
    gap: 22px;
  }
  .brand-dot {
    width: 44px; height: 44px;
    border-radius: 50%;
    background: var(--accent);
  }
  .brand-name {
    font-size: 72px;
    line-height: 1;
    color: var(--ink);
    letter-spacing: 2px;
  }
  .service {
    position: absolute;
    display: flex;
    align-items: center;
    white-space: nowrap;
    line-height: 1;
  }
  .service .star { flex: none; fill: var(--accent); }
  .service-main { font-size: 92px; letter-spacing: 4px; }
  .service-sub { font-size: 50px; letter-spacing: 3px; }
  .service-small { font-size: 30px; letter-spacing: 2px; }
  .mowing { left: 94px; top: 440px; gap: 26px; }
  .fertilization { left: 96px; top: 550px; gap: 30px; }
  .aeration { left: 646px; top: 440px; gap: 26px; }
  .bed-tree { left: 652px; top: 568px; gap: 24px; }
  .and-more {
    position: absolute;
    right: 78px;
    top: 640px;
    font-family: "Oswald", sans-serif;
    font-weight: 500;
    font-size: 28px;
    letter-spacing: 2px;
    text-transform: uppercase;
  }
  .phone {
    position: absolute;
    left: 0; right: 0;
    top: 690px;
    text-align: center;
    font-family: "Oswald", sans-serif;
    font-weight: 500;
    font-size: 96px;
    letter-spacing: 8px;
    line-height: 1;
  }
  .email {
    position: absolute;
    left: 0; right: 0;
    top: 818px;
    text-align: center;
    font-family: "Oswald", sans-serif;
    font-weight: 400;
    font-size: 40px;
    line-height: 1;
  }
  .email-label { color: var(--accent); }
</style>
</head>
<body>
<main class="sign">
  <div class="brand">
    <span class="brand-dot"></span>
    <span class="brand-name">Tidy Turf Co</span>
  </div>

  <div class="service mowing">
    <svg class="star" width="36" height="36" viewBox="0 0 24 24" aria-hidden="true"><polygon points="12,1 15,9 23.5,9 16.5,14 19,22.5 12,17.5 5,22.5 7.5,14 0.5,9 9,9"/></svg>
    <span class="service-main">Mowing</span>
  </div>
  <div class="service fertilization">
    <svg class="star" width="34" height="34" viewBox="0 0 24 24" aria-hidden="true"><polygon points="12,1 15,9 23.5,9 16.5,14 19,22.5 12,17.5 5,22.5 7.5,14 0.5,9 9,9"/></svg>
    <span class="service-sub">Fertilization</span>
  </div>
  <div class="service aeration">
    <svg class="star" width="36" height="36" viewBox="0 0 24 24" aria-hidden="true"><polygon points="12,1 15,9 23.5,9 16.5,14 19,22.5 12,17.5 5,22.5 7.5,14 0.5,9 9,9"/></svg>
    <span class="service-main">Aeration</span>
  </div>
  <div class="service bed-tree">
    <svg class="star" width="34" height="34" viewBox="0 0 24 24" aria-hidden="true"><polygon points="12,1 15,9 23.5,9 16.5,14 19,22.5 12,17.5 5,22.5 7.5,14 0.5,9 9,9"/></svg>
    <span class="service-small">Bed &amp; tree maintenance</span>
  </div>
  <p class="and-more">and more.</p>

  <p class="phone">816-402-7761</p>
  <p class="email"><span class="email-label">Email:</span> tidyturfco@fernmail.com</p>
</main>
</body>
</html>
```